Flyer-Design für Blog gesucht
Zielgruppe
Ich betreibe momentan einen Fotoria -Blog KlangWEIT7 unter dem Motto Wohlbefinden für DEINE Sinne. https://Fotoria.example/klangweit7/ www.freundnetz.example/KlangWEIT7/ Hier wurde bisher der Inhalt in die Rubriken SEHEN (Augenweiden), FÜHLEN (Körpergefühl/- Wahrnehmung), SCHMECKEN (Gaumenfreuden) untergliedert. Bewusstsein, Achtsamkeit, Zufriedenheit.
Ich möchte nun zukünftig Veranstaltungen und Kurse anbieten. Beginnen werde ich mit einem Kinderkurs der pro Kursstunde aus einem Tanz- und Achtsamkeitspart bestehen wird. Genauere Details sind dem anhängenden PDF zu entnehmen.
Aufgabenstellung
Dass einerseits KlangWEIT7 im Flyer erläutert wird und jedoch vprrangig gezielt der Kinderkurs beworben ist.
Die Logo-Farbe berücksichtigt wird.
Bei Bildquellix habe ich neutrale Lineart - Bilder herausgesucht, die mir für den Kinderkurs gut gefallen würden, da sie den aktiven und entspannteren Kurspart gut verdeutlichen, recht geschlechtsneutral und fröhlich wirken. Bsp.: 4827193056,
Es können jedoch gerne andere Bilder verwendet werden.
Ich habe ebenfalls mal Portraits von mir beigefügt. Damit die Kinder evtl. sehen können wer sie überhaupt im Kurs begleitet. Vielleicht kann man hiervon eines verwenden ? Wobei ich gerne auch andere passendere Bilder zu Verfügung stellen könnte.

```html
<!DOCTYPE html>
<html lang="de">
<head>
<meta charset="utf-8">
<title>KIDS Dance &amp; MORE – KlangWEIT7</title>
<link rel="stylesheet" href="https://fonts.googleapis.com/css2?family=Arimo:ital,wght@0,400;0,700;1,400;1,700&display=swap">
<style>
  :root {
    --mint: #a9cdc7;
    --mint-pale: #e6f1ef;
    --mint-shadow: #7fa39d;
    --ink: #1e1e1e;
    --grey: #6c6c6c;
    --white: #ffffff;
  }
  html, body { margin: 0; padding: 0; overflow: hidden; background: var(--white); }
  .flyer {
    position: relative; width: 920px; height: 1200px; overflow: hidden;
    background: var(--white); font-family: "Arimo", Arial, sans-serif; color: var(--ink);
  }
  .flyer > * { position: absolute; }
  .backdrop { left: 0; top: 0; width: 920px; height: 1200px; }

  .brand-badge {
    left: 30px; top: 15px; width: 176px; height: 176px; border-radius: 50%;
    background: var(--mint); display: flex; align-items: center; justify-content: center;
    color: var(--white); font-size: 27px; font-weight: 400;
  }
  .course-badge {
    left: 756px; top: 56px; width: 140px; height: 140px; border-radius: 50%;
    background: var(--white); display: flex; align-items: center; justify-content: center;
    color: var(--grey); font-size: 20px; font-weight: 400;
  }
  .hero-art {
    left: 40px; top: 20px; width: 660px; height: 340px;
    background: radial-gradient(ellipse at 55% 45%, var(--mint-pale) 0%, #f4f9f8 60%, var(--white) 100%);
    border-radius: 45% 45% 35% 35%;
  }

  .title {
    left: 23px; top: 383px; margin: 0; font-size: 51px; font-weight: 700; letter-spacing: .5px;
    color: var(--mint); text-shadow: 2px 3px 3px var(--mint-shadow);
  }
  .age-badge {
    left: 636px; top: 364px; width: 176px; height: 176px; border-radius: 50%;
    background: var(--mint); box-shadow: 3px 4px 6px rgba(0,0,0,.25);
    color: var(--white); text-align: center; font-size: 38px; line-height: 43px;
    display: flex; flex-direction: column; justify-content: center;
  }

  .body-copy { left: 24px; top: 460px; width: 720px; font-size: 16px; line-height: 16.1px; letter-spacing: .2px; }
  .body-copy p { margin: 0 0 16px; }
  .tagline { left: 24px; top: 767px; margin: 0; font-size: 16px; font-style: italic; }

  .benefits { top: 800px; font-size: 16px; line-height: 16.1px; }
  .benefits p { margin: 0 0 16px; }
  .benefits ul { margin: 0; padding: 0; list-style: none; }
  .benefits li { position: relative; }
  .benefits li::before {
    content: ""; position: absolute; left: -10px; top: 10px; width: 4px; height: 4px;
    border-radius: 50%; background: var(--mint);
  }
  .benefits--dance { left: 24px; width: 340px; }
  .benefits--mind { left: 379px; width: 300px; }

  .closing { left: 22px; top: 965px; margin: 0; font-size: 16px; font-style: italic; }
  .dates { left: 22px; top: 997px; font-size: 16px; font-weight: 700; }
  .dates-line { left: 100px; width: 544px; height: 0; border-top: 1px solid var(--grey); }

  .trainer-photo {
    left: 684px; top: 880px; width: 205px; height: 200px; border-radius: 50%;
    background: radial-gradient(circle at 50% 45%, #c9a48c 0%, #8a6048 45%, #e6e6e6 80%);
  }
  .qualifications {
    left: 656px; top: 1078px; width: 264px; height: 50px; background: var(--white);
    font-size: 12.5px; line-height: 14.5px; text-align: center;
    display: flex; flex-direction: column; justify-content: center;
  }
  .greeting {
    left: 656px; top: 1136px; width: 264px; text-align: center; font-size: 17.5px; line-height: 19px;
  }

  .signup {
    left: 23px; top: 1085px; margin: 0; font-size: 19.5px; line-height: 21px; font-weight: 700; color: var(--grey);
  }
  .parents-note {
    left: 23px; top: 1141px; margin: 0; font-size: 13.5px; line-height: 16px; font-style: italic; color: var(--ink);
  }
</style>
</head>
<body>
<main class="flyer">
  <svg class="backdrop" viewBox="0 0 920 1200" aria-hidden="true">
    <path fill="var(--mint)" d="M776 0 L920 0 L920 1200 L0 1200 L0 1052 C250 1078 500 1072 690 1037 C780 1010 812 955 812 890 C812 760 760 560 724 400 C712 300 714 150 776 0 Z"/>
  </svg>

  <div class="hero-art" role="img" aria-label="Lineart-Illustration: zwei fröhlich tanzende und springende Kinder in einer durchgehenden Linie"></div>
  <div class="brand-badge">KlangWEIT7</div>
  <div class="course-badge">Kinderkurs</div>

  <h1 class="title">KIDS Dance &amp; MORE</h1>
  <div class="age-badge"><span>Alter:</span><span>6 -10</span><span>Jahre</span></div>

  <section class="body-copy">
    <p>In unserer Kursstunde werden in Kleingruppen (m/w)</p>
    <p><strong>Tanz, bewusste Körperwahrnehmung und Entspannung</strong></p>
    <p>kindgerecht und mit viel Lebensfreude vereint.</p>
    <p>Im ersten Teil jeder Kursstunde findet unsere <strong>Tanz-Einheit mit HIPHOP / Pop-Dance</strong><br>
    Inhalten statt. Hier können sich die Kids mit Freude zu den Beats bewegen und<br>
    studieren gemeinsam eine Choreographie ein. Im zweiten Kursteil jeder Stunde werden<br>
    die Themen Achtsamkeit, Selbstwahrnehmung und Entspannung kindgerecht eingebunden.<br>
    Auch schon Kinder und Jugendliche sind oft angespannt, ängstlich oder aggressiv.<br>
    Viele leiden zusätzlich an Bauch-Kopfschmerzen, Rückenschmerzen oder haben<br>
    Schlafprobleme. Zu viele Ansprüche und verschiedenartige Einflüsse führen schon<br>
    früh zu Überforderung des vegetativen Nervensystems (Reizüberflutung), was sich<br>
    u.a. durch Unruhe und Aufmerksamkeitsschwierigkeiten bemerkbar macht.<br>
    Auslöser dieser Symptome können des Weiteren Schulstress, soziale Konflikte<br>
    oder Bewegungsmangel etc. sein.</p>
  </section>

  <p class="tagline">Jetzt ist verständlich, weshalb wir diesen Kurs anbieten!</p>

  <section class="benefits benefits--dance">
    <p>Tanzen wirkt befreiend und fördert:</p>
    <ul>
      <li>das Selbstbewusstsein,</li>
      <li>die koordinativen/motorischen Fähigkeiten,</li>
      <li>die Körperhaltung,</li>
      <li>den Ausgleich muskulärer Dysbalancen.</li>
    </ul>
  </section>
  <section class="benefits benefits--mind">
    <p>Durch verschiedene Methoden und Themen<br>wird den Kids in der zweiten Kurshälfte:</p>
    <ul>
      <li>die Selbstwahrnehmung ihrer<br>Gefühle und Körpersignale verdeutlicht,</li>
      <li>ihr Selbstwert bewusst gemacht</li>
      <li>sie dabei schrittweise begleitet emotions-<br>bezogene Bewältigungskompetenz zu<br>erlangen.</li>
    </ul>
  </section>

  <p class="closing">Die eindeutig positive Auswirkung beeinflusst ihre körperliche und geistige Entwicklung.</p>
  <div class="dates">Termine:</div>
  <div class="dates-line" style="top:1011px"></div>
  <div class="dates-line" style="top:1035px"></div>

  <div class="trainer-photo" role="img" aria-label="Porträtfoto der Kursleiterin"></div>
  <div class="qualifications">
    <span>Meine Qualifikationen:</span>
    <span>Trainerin für Fitness, Gesundheit,</span>
    <span>Achtsamkeit sowie Bewegungspädagogin</span>
  </div>
  <div class="greeting">Ich freue mich auf euch!<br>Euere Mareike</div>

  <p class="signup">Anmeldung und weitere Informationen unter:<br>Klang.WEIT7@postfach.example oder www.KlangWEIT7.example</p>
  <p class="parents-note">(Die Eltern erhalten vor Kursbeginn nähere Informationen zum Kursinhalt und sind bspw.<br>eingeladen ihre Kinder bei der ein oder anderen Übung im Alltag zu unterstützen.)</p>
</main>
</body>
</html>
```